Stylish Business Cards Wanted

- DOUBLE SIDED Design Required -

High end, edgy cards for a corporate and personal stylist. Must include logo,
Name: Belinda Marsh
Title: Director and Stylist
telephone : +61 8 8417 2950
email: belinda@thewardrobeledger.com
website: thewardrobeledger.com
Tag: Corporate Workwear & Uniform Specialist | Personal Stylist
Would like nice icons for telephone, email, website

Target Market(s)

Businesses wanting stylish uniforms, people wanting stylish wardrobes

Industry/Entity Type

Corporate Workwear Stylist

Contact Information for Business Card

I would like black, white and gold foiling incorporated in the design - possibly a touch of the other colours on my branding guide attached Name: Belinda Marsh Title: Director and Stylist telephone : +61 8 8417 2950 email: belinda@thewardrobeledger.com website: thewardrobeledger.com Tag: Corporate Workwear & Uniform Specialist | Personal Stylist Would like nice icons for telephone, email, website

Font styles to use
Other font styles liked:
• Raleway

Colors

Designer to choose colors to be used in the design.

Requirements
Must have
• Gold foil accents

```html
<!DOCTYPE html>
<html lang="en">
<head>
<meta charset="utf-8">
<title>The Wardrobe Ledger – Business Cards</title>
<link rel="stylesheet" href="https://fonts.googleapis.com/css2?family=Arimo:wght@400;700&family=Great+Vibes&display=swap">
<style>
  :root {
    --page: #e9e9e8;
    --card: #2a2a2a;
    --card-back: #262626;
    --gloss: #1b1b1b;
    --white: #f4f4f2;
    --gold: #c9a24a;
    --divider: #8a8a8a;
  }
  * { margin: 0; padding: 0; box-sizing: border-box; }
  html, body { width: 1200px; height: 801px; overflow: hidden; }
  body {
    background: var(--page);
    font-family: "Arimo", Arial, sans-serif;
    position: relative;
  }
  .card {
    position: absolute;
    top: 241px;
    width: 540px;
    height: 320px;
    border-radius: 3px;
    box-shadow: 0 6px 18px rgba(0,0,0,0.18);
    overflow: hidden;
  }
  .card--front { left: 45px; background: var(--card); }
  .card--back { left: 615px; background: var(--card-back); }

  .brand {
    position: absolute;
    top: 70px;
    left: 0;
    width: 100%;
    text-align: center;
    color: var(--white);
    font-weight: 700;
    letter-spacing: 0.04em;
    line-height: 1.1;
  }
  .brand__small { display: block; font-size: 14px; letter-spacing: 0.5em; }
  .brand__large { display: block; font-size: 38px; }

  .identity {
    position: absolute;
    left: 40px;
    bottom: 52px;
    width: 220px;
    text-align: right;
  }
  .identity__name {
    font-family: "Great Vibes", cursive;
    color: var(--gold);
    font-size: 40px;
    line-height: 1;
  }
  .identity__title {
    color: var(--white);
    font-size: 14px;
    margin-top: 4px;
  }
  .divider {
    position: absolute;
    left: 282px;
    bottom: 44px;
    width: 1px;
    height: 78px;
    background: var(--divider);
  }
  .contacts {
    position: absolute;
    left: 300px;
    bottom: 48px;
    list-style: none;
    color: var(--white);
    font-size: 12.5px;
  }
  .contacts li { display: flex; align-items: center; gap: 7px; margin-top: 6px; white-space: nowrap; }
  .contacts svg { width: 11px; height: 11px; flex: none; }
  .contacts .accent { color: var(--gold); }

  .back-mark {
    position: absolute;
    inset: 0;
    display: flex;
    flex-direction: column;
    justify-content: center;
    align-items: center;
    color: var(--gloss);
    font-weight: 700;
    line-height: 1;
  }
  .back-mark__small { font-size: 30px; letter-spacing: 0.5em; }
  .back-mark__large { font-size: 78px; letter-spacing: 0.02em; }
</style>
</head>
<body>
  <section class="card card--front">
    <div class="brand">
      <span class="brand__small">THE</span>
      <span class="brand__large">Wardrobe Ledger</span>
    </div>

    <div class="identity">
      <p class="identity__name">Belinda Marsh</p>
      <p class="identity__title">Director and Stylist</p>
    </div>

    <div class="divider"></div>

    <ul class="contacts">
      <li>
        <svg viewBox="0 0 12 12" aria-hidden="true"><path fill="#c9a24a" d="M2.5 1l2 2.2-1 1.3c.8 1.6 1.9 2.7 3.5 3.5l1.3-1 2.2 2-1.2 1.6C5 10.4 1.6 7 .9 2.2z"/></svg>
        +61 8 8417 2950
      </li>
      <li>
        <svg viewBox="0 0 12 12" aria-hidden="true"><rect x="0.5" y="2" width="11" height="8" fill="#c9a24a"/><path d="M0.8 2.4L6 6.6l5.2-4.2" fill="none" stroke="#2a2a2a" stroke-width="1"/></svg>
        belinda@thewardrobeledger.com
      </li>
      <li>
        <svg viewBox="0 0 12 12" aria-hidden="true"><circle cx="6" cy="6" r="5.5" fill="#c9a24a"/><ellipse cx="6" cy="6" rx="2.3" ry="5.3" fill="none" stroke="#2a2a2a" stroke-width="0.9"/><path d="M0.7 6h10.6" stroke="#2a2a2a" stroke-width="0.9"/></svg>
        www.<span class="accent">thewardrobeledger</span>.com
      </li>
    </ul>
  </section>

  <section class="card card--back">
    <div class="back-mark">
      <span class="back-mark__small">THE</span>
      <span class="back-mark__large">Wardrobe</span>
      <span class="back-mark__large">Ledger</span>
    </div>
  </section>
</body>
</html>
```